Fernwood Chiropractic
letterhead/business cards
Project: Fernwood Chiropractic
Fernwood Chiropractic - Health
Creative Brief
Professional
Dr. Gavin P. Holcombe
Chiropractor
4817 Dunmore Road Building 2, Suite C-21 Philadelphia, PA 19144
drholcombe@fernwoodchiro-example.com
www.fernwoodchiro-example.com

```html
<!DOCTYPE html>
<html lang="en">
<head>
<meta charset="UTF-8">
<title>Fernwood Chiropractic – Business Cards</title>
<link href="https://fonts.googleapis.com/css2?family=Cinzel:wght@500&family=Open+Sans:wght@400;600&display=swap" rel="stylesheet">
<style>
  :root{
    --backdrop:#e9e6e1;
    --card-white:#ffffff;
    --card-blue-deep:#1b2690;
    --card-blue:#2f44c6;
    --brand-blue:#2b8fd4;
    --brand-light:#bfe1fb;
    --leaf-green:#7cc243;
    --leaf-green-soft:#a8d86f;
    --ink-gray:#6b6f75;
    --rule-gray:#d9dde2;
  }
  *{box-sizing:border-box;margin:0;padding:0}
  html,body{width:1200px;height:1023px;overflow:hidden}
  body{background:var(--backdrop);font-family:"Open Sans",sans-serif;position:relative}
  .card{
    position:absolute;left:340px;width:520px;height:297px;
    border-radius:4px;box-shadow:0 8px 24px rgba(0,0,0,.18);overflow:hidden;
  }
  .card--front{top:150px;background:var(--card-white)}
  .card--back{top:576px;background:linear-gradient(135deg,var(--card-blue-deep),var(--card-blue) 60%,var(--card-blue-deep))}

  .mark-area{
    position:absolute;left:38px;top:92px;width:150px;height:150px;border-radius:50%;
    background:radial-gradient(circle at 45% 40%,var(--leaf-green-soft),var(--leaf-green));
  }
  .front-info{position:absolute;left:232px;top:34px;right:28px}
  .brand-name{
    font-family:"Cinzel",serif;font-weight:500;color:var(--brand-blue);
    font-size:22px;letter-spacing:1px;line-height:1.1;
  }
  .doctor{margin-top:20px;color:var(--brand-blue);font-size:15px;font-weight:600}
  .role{color:var(--ink-gray);font-size:11px;margin-top:2px}
  .rule{height:1px;background:var(--rule-gray);margin:12px 0}
  .contact{list-style:none;color:var(--ink-gray);font-size:10px;line-height:1.45}
  .contact li{display:flex;align-items:flex-start;gap:7px;margin-bottom:4px}
  .contact svg{flex:none;width:10px;height:10px;margin-top:2px;fill:var(--brand-blue)}

  .back-lockup{position:absolute;inset:0;display:flex;flex-direction:column;align-items:center;justify-content:center;gap:18px}
  .back-lockup .dot{width:96px;height:96px;border-radius:50%;background:var(--leaf-green)}
  .back-lockup .brand-name{color:var(--brand-light);font-size:28px;letter-spacing:2px}
</style>
</head>
<body>

<section class="card card--front" aria-label="Business card front">
  <div class="mark-area" role="img" aria-label="Practice emblem area"></div>
  <div class="front-info">
    <h1 class="brand-name">FERNWOOD CHIROPRACTIC</h1>
    <p class="doctor">Dr. Gavin P. Holcombe</p>
    <p class="role">Chiropractor</p>
    <div class="rule"></div>
    <ul class="contact">
      <li><svg viewBox="0 0 10 10"><path d="M5 0a3.5 3.5 0 0 0-3.5 3.5C1.5 6 5 10 5 10s3.5-4 3.5-6.5A3.5 3.5 0 0 0 5 0zm0 5a1.4 1.4 0 1 1 0-2.8A1.4 1.4 0 0 1 5 5z"/></svg>
        <span>4817 Dunmore Road Building 2, Suite C-21<br>Philadelphia, PA 19144</span></li>
      <li><svg viewBox="0 0 10 10"><path d="M2 0l2 2.5-1 1.2a6 6 0 0 0 3.3 3.3l1.2-1L10 8l-1.3 1.6C4.5 10 0 5.5.4 1.3z"/></svg>
        <span>Phone: (215) 555-0147 &nbsp; Fax: (215) 555-0148</span></li>
      <li><svg viewBox="0 0 10 10"><path d="M0 2h10v6H0zM0 2l5 3.5L10 2" stroke="#fff" stroke-width=".8"/></svg>
        <span>drholcombe@fernwoodchiro-example.com</span></li>
      <li><svg viewBox="0 0 10 10"><circle cx="5" cy="5" r="4.5"/><path d="M.5 5h9M5 .5c-2 2.5-2 6.5 0 9M5 .5c2 2.5 2 6.5 0 9" stroke="#fff" stroke-width=".7" fill="none"/></svg>
        <span>www.fernwoodchiro-example.com</span></li>
    </ul>
  </div>
</section>

<section class="card card--back" aria-label="Business card back">
  <div class="back-lockup">
    <div class="dot"></div>
    <h2 class="brand-name">FERNWOOD CHIROPRACTIC</h2>
  </div>
</section>

</body>
</html>
```